Financial Workshop for Hollister Wealth

Postcard to comply with RMPS. Invitation to workshop for 55+ senior community.
"Estate Conservation Strategies and Legacy Planning"
Building a sound and lasting retirement portfolio with a focus on growth and asset protection.
Developing investment objectives
Understanding risk adversity
Preserving assets
Conservative growth strategies for saving and investing
Planning for uncovered health care costs
Estate planning
Dale Whitford, Chartered Money Counselorâ„¢

add to the text (bullets) after Estate Planning (on same line) and Wealth Transfer Strategies Thank you Added Friday, October 13, 2017

Target Market(s)

Seniors

Industry/Entity Type

Financial

Font styles to use
Sans Serif

Colors

Designer to choose colors to be used in the design.

Requirements
Must have
• Logo
• Eye-catching images
• Easy to read geared for seniors
• Upscale professional look
• Afresh new look from previous samples sent.
Nice to have
• Something that stands out among the many postcard mail pieces they will get.
Should not have
• aside from logo/photo samples are an example of previous workshops and should not be reused.

```html
<!DOCTYPE html>
<html lang="en">
<head>
<meta charset="utf-8">
<title>Hollister Wealth – Workshop Postcard</title>
<link href="https://fonts.googleapis.com/css2?family=Montserrat:wght@500;600&family=Open+Sans:ital,wght@0,400;0,600;0,700;1,600&family=Saira+Condensed:wght@600;700&display=swap" rel="stylesheet">
<style>
:root{
  --bg:#9cb1c6;
  --card:#eef1f3;
  --card-shade:#d9dee2;
  --slate:#5f6f79;
  --slate-dark:#46545d;
  --ink:#3b4247;
  --navy:#23307a;
  --rule:#a9b3ba;
  --white:#ffffff;
}
*{margin:0;padding:0;box-sizing:border-box}
html,body{width:1200px;height:696px;overflow:hidden;background:var(--bg)}
.stage{position:relative;width:1200px;height:696px}
.postcard{position:absolute;top:158px;width:570px;height:380px;background:linear-gradient(135deg,var(--white),var(--card) 55%,var(--card-shade));overflow:hidden;font-family:"Open Sans",sans-serif;color:var(--ink)}
.back{left:20px}
.front{left:610px}

/* back side */
.portrait{position:absolute;left:24px;top:20px;width:78px;height:78px;border-radius:50%;border:2px solid var(--navy);background:radial-gradient(circle at 50% 40%,#c9a08c,#6b5a55 60%,#2f3440)}
.advisor-name{position:absolute;left:118px;top:34px;font-family:"Montserrat",sans-serif;font-weight:600;font-size:28px;color:var(--slate-dark)}
.advisor-title{position:absolute;left:118px;top:70px;font-family:"Montserrat",sans-serif;font-weight:500;font-size:12px;color:var(--slate)}
.bio{position:absolute;left:30px;top:108px;width:330px;font-size:10px;font-style:italic;font-weight:600;line-height:1.75;text-align:justify;text-align-last:center}
.topics-band{position:absolute;left:30px;top:202px;width:180px;height:24px;background:var(--slate);color:var(--white);border-radius:0 0 8px 0;font-family:"Saira Condensed",sans-serif;font-weight:700;font-size:15px;letter-spacing:1px;padding:1px 0 0 20px}
.topics{position:absolute;left:30px;top:236px;list-style:none;font-size:11px;font-weight:600;line-height:1.85}
.topics li::before,.points .item::before{content:"";display:inline-block;width:7px;height:7px;border-radius:50%;background:radial-gradient(circle at 35% 35%,#e6e9eb,var(--slate-dark));margin-right:7px;vertical-align:0}
.contact{position:absolute;left:30px;top:340px;font-size:13px;color:var(--ink)}
.contact b{color:var(--navy);font-weight:700}
.indicia{position:absolute;left:468px;top:26px;width:78px;height:58px;border:1px solid var(--slate);font-size:7.5px;line-height:1.25;text-align:center;padding-top:4px;color:var(--ink)}
.mail-lines{position:absolute;left:360px;top:190px;width:190px}
.mail-lines span{display:block;height:1px;background:var(--rule);margin-bottom:26px}

/* front side */
.photo{position:absolute;left:290px;top:0;width:280px;height:380px;background:radial-gradient(ellipse at 60% 40%,#d9dcdd,#8e9396 55%,#5d6366)}
.divider{position:absolute;left:0;top:0}
.brand{position:absolute;left:26px;top:28px;display:flex;align-items:center;gap:10px;font-weight:600;font-size:22px;letter-spacing:3px;color:var(--navy)}
.brand i{display:block;width:20px;height:20px;background:var(--navy)}
.invite{position:absolute;left:94px;top:128px;width:210px;height:44px;background:linear-gradient(#6d7c85,var(--slate-dark));border:2px solid #c9d0d4;outline:1px solid var(--slate-dark);color:var(--white);font-family:"Saira Condensed",sans-serif;font-weight:700;font-size:14px;letter-spacing:1px;line-height:1.2;text-align:center;padding-top:3px}
.headline{position:absolute;left:14px;top:180px;width:290px;text-align:center;font-family:"Saira Condensed",sans-serif;font-weight:700;font-size:21px;line-height:1.2;color:var(--slate-dark)}
.points{position:absolute;left:20px;top:240px;width:330px;list-style:none;font-size:8.5px;font-weight:700;line-height:16px;color:var(--ink)}
.points li{padding-left:14px;text-indent:-14px}
.points .item{margin-right:8px}
.email-band{position:absolute;left:0;top:350px;width:215px;height:22px;background:var(--slate-dark);border-radius:0 10px 0 0;color:var(--white);font-size:11.5px;font-weight:600;padding:2px 0 0 16px}
</style>
</head>
<body>
<div class="stage">

  <section class="postcard back">
    <div class="portrait" role="img" aria-label="Portrait photo of the advisor"></div>
    <h1 class="advisor-name">Dale Whitford</h1>
    <p class="advisor-title">CHARTERED MONEY COUNSELOR™</p>
    <p class="bio">Dale Whitford is a CHARTERED MONEY COUNSELOR™, specializing in asset management of IRA, retirement and investment accounts. Whitford Advisors, LLC is an independent Registered Investment Advisor with a low cost, commission free business model. Concierge level service is provided to Maple Ridge Commons residents.</p>
    <div class="topics-band">Workshop Topics:</div>
    <ul class="topics">
      <li>How hidden costs drag down investment results</li>
      <li>Maximizing income flow in Retirement</li>
      <li>Growing and Protecting Retirement Assets</li>
      <li>Estate Conservation Strategies</li>
    </ul>
    <p class="contact"><b>A:</b> 48 Linden Brook Lane, Fairhaven, NC 27590 | <b>P:</b> 555-210-0148 | <b>F:</b> (555) 210-0199</p>
    <div class="indicia">PRSRT STD<br>ECRWSS<br>U.S.POSTAGE<br>PAID<br>RMPS RETAIL</div>
    <div class="mail-lines"><span></span><span></span><span></span><span></span></div>
  </section>

  <section class="postcard front">
    <div class="photo" role="img" aria-label="Photo of a smiling senior couple embracing outdoors"></div>
    <svg class="divider" width="570" height="380" viewBox="0 0 570 380" aria-hidden="true">
      <defs>
        <linearGradient id="panel" x1="0" y1="0" x2="1" y2="1">
          <stop offset="0" stop-color="#ffffff"/>
          <stop offset=".6" stop-color="#eceff1"/>
          <stop offset="1" stop-color="#d3d9dd"/>
        </linearGradient>
      </defs>
      <path d="M300 0 C305 90 345 180 360 260 C368 310 362 350 352 380" fill="none" stroke="#d9dee2" stroke-width="14" transform="translate(22 0)"/>
      <path d="M300 0 C305 90 345 180 360 260 C368 310 362 350 352 380" fill="none" stroke="#5f6f79" stroke-width="14" transform="translate(8 0)"/>
      <path d="M0 0 H300 C305 90 345 180 360 260 C368 310 362 350 352 380 H0Z" fill="url(#panel)"/>
      <path d="M150 0 C215 35 220 95 270 130 C255 90 265 40 292 0Z" fill="#ffffff" opacity=".7"/>
    </svg>
    <div class="brand"><i></i>HOLLISTER WEALTH</div>
    <div class="invite">Invitation to workshop for<br>55+ senior community.</div>
    <h2 class="headline">Estate Conservation Strategies<br>and Legacy Planning</h2>
    <ul class="points">
      <li><span class="item">Building a sound and lasting retirement portfolio with a focus on growth and asset protection.</span></li>
      <li><span class="item">Conservative growth strategies for saving and investing</span></li>
      <li><span class="item">Planning for uncovered health care costs</span></li>
      <li><span class="item">Developing investment objectives</span><span class="item">Understanding risk adversity</span></li>
      <li><span class="item">Preserving assets</span><span class="item">Estate planning</span><span class="item">Wealth Transfer Strategies</span></li>
    </ul>
    <div class="email-band">dale@hollisterwealth.com</div>
  </section>

</div>
</body>
</html>
```